Design einer Schachtel für hochwertigen Christstollen
Zielgruppe
Wir benötigen eine weihnachtliche Geschenk - Schachtel für hochwertigen Christstollen. Das Produkt soll nicht genannt werden, nur Weihnachtssprüche wie 'Frohe Weihnachten' sollen darauf stehen. Zielgruppe sind Firmen, die diese an Ihre Mitarbeiter/Kunden/Geschäftspartner überreicht
Aufgabenstellung
Eine Druckstandskizze ist angehangen - das Design soll weihnachtlich sein, ggf. eher modern darf aber klassische Elemente beinhalten - ein elegantes, zeitloses Design. Das Produkt soll nicht genannt werden, nur Weihnachtssprüche wie 'Frohe Weihnachten' - evtl. auch in verschiedenen Sprachen - sollen darauf stehen.

```html
<!DOCTYPE html>
<html lang="de">
<head>
<meta charset="utf-8">
<title>Weihnachtliche Geschenkschachtel – Stanzbogen</title>
<link rel="stylesheet" href="https://fonts.googleapis.com/css2?family=Italianno&family=Almendra:wght@700&family=Questrial&display=swap">
<style>
  :root {
    --backdrop: #b8b8b8;
    --paper: #ffffff;
    --panel-light: #f3f3f1;
    --purple-light: #4b2a76;
    --purple-mid: #3b2461;
    --purple-dark: #231a38;
    --gold: #c9a47a;
    --die-line: #e2549c;
    --logo-grey: #d8d8d8;
    --star: #ffffff;
  }
  html, body {
    margin: 0;
    padding: 0;
    width: 1200px;
    height: 1200px;
    overflow: hidden;
    background: var(--paper);
  }
  .dieline-sheet { display: block; width: 1200px; height: 1200px; }
  .greeting { font-family: "Italianno", cursive; fill: var(--gold); font-size: 66px; }
  .tagline { font-family: "Italianno", cursive; fill: var(--gold); font-size: 22px; }
  .headline { font-family: "Almendra", serif; font-weight: 700; fill: var(--star); font-size: 23px; }
  .logo-placeholder { font-family: "Questrial", sans-serif; fill: var(--logo-grey); font-size: 40px; letter-spacing: 2px; }
  .cut { fill: var(--paper); stroke: var(--die-line); stroke-width: 1.2; }
  .halo { fill: var(--paper); stroke: var(--paper); stroke-width: 14; stroke-linejoin: round; }
  .star { fill: var(--star); opacity: .85; }
</style>
</head>
<body>
<svg class="dieline-sheet" viewBox="0 0 1200 1200" xmlns="http://www.w3.org/2000/svg">
  <defs>
    <linearGradient id="lid-gradient" x1="0" y1="1" x2="0.35" y2="-0.3">
      <stop offset="0" stop-color="var(--purple-mid)"/>
      <stop offset="0.45" stop-color="var(--purple-light)"/>
      <stop offset="1" stop-color="var(--purple-dark)"/>
    </linearGradient>
    <linearGradient id="band-gradient" x1="0" y1="0" x2="1" y2="0.3">
      <stop offset="0" stop-color="var(--purple-light)"/>
      <stop offset="0.55" stop-color="var(--purple-mid)"/>
      <stop offset="1" stop-color="var(--purple-dark)"/>
    </linearGradient>
    <linearGradient id="snow-gradient" x1="0" y1="0" x2="0" y2="1">
      <stop offset="0" stop-color="#ffffff" stop-opacity="0"/>
      <stop offset="0.55" stop-color="#ffffff" stop-opacity="0.45"/>
      <stop offset="1" stop-color="#ffffff" stop-opacity="0.95"/>
    </linearGradient>

    <g id="lid-artwork">
      <rect width="523" height="218" fill="url(#lid-gradient)"/>
      <g class="star">
        <circle cx="5" cy="153" r="1.4"/><circle cx="23" cy="150" r="1.2"/><circle cx="45" cy="156" r="1.2"/>
        <circle cx="65" cy="160" r="1.5"/><circle cx="100" cy="152" r="1.2"/><circle cx="140" cy="163" r="1.3"/>
        <circle cx="180" cy="165" r="1.2"/><circle cx="220" cy="170" r="1.4"/><circle cx="262" cy="164" r="1.2"/>
        <circle cx="300" cy="168" r="1.2"/><circle cx="335" cy="152" r="1.5"/><circle cx="360" cy="140" r="1.2"/>
        <circle cx="380" cy="120" r="1.3"/><circle cx="410" cy="110" r="1.2"/><circle cx="440" cy="128" r="1.4"/>
        <circle cx="470" cy="113" r="1.2"/><circle cx="498" cy="130" r="1.3"/><circle cx="515" cy="112" r="1.2"/>
        <circle cx="36" cy="173" r="1.1"/><circle cx="236" cy="148" r="1.1"/><circle cx="290" cy="140" r="1.2"/>
        <circle cx="120" cy="170" r="1.1"/><circle cx="400" cy="95" r="1.1"/><circle cx="460" cy="103" r="1.1"/>
      </g>
      <text class="greeting" x="50" y="160" transform="rotate(-8 50 160)" textLength="416" lengthAdjust="spacingAndGlyphs">Frohe Weihnachten!</text>
    </g>

    <g id="front-artwork">
      <rect width="522" height="296" fill="var(--panel-light)"/>
      <polygon points="83,0 228,0 438,296 293,296" fill="url(#band-gradient)"/>
      <g class="star">
        <circle cx="130" cy="45" r="1.2"/><circle cx="160" cy="80" r="1.4"/><circle cx="190" cy="60" r="1.1"/>
        <circle cx="200" cy="110" r="1.2"/><circle cx="255" cy="200" r="1.3"/><circle cx="300" cy="180" r="1.1"/>
        <circle cx="340" cy="215" r="1.4"/><circle cx="360" cy="240" r="1.2"/><circle cx="385" cy="255" r="1.3"/>
        <circle cx="400" cy="275" r="1.2"/><circle cx="240" cy="170" r="1.1"/><circle cx="320" cy="200" r="1.2"/>
        <circle cx="60" cy="200" r="1" opacity=".5"/><circle cx="120" cy="250" r="1" opacity=".5"/><circle cx="460" cy="80" r="1" opacity=".5"/>
      </g>
      <rect x="198" y="184" width="156" height="112" rx="6" fill="url(#snow-gradient)" role="img" aria-label="Silhouette verschneiter Tannenbäume"/>
    </g>
  </defs>

  <rect x="36" y="41" width="1136" height="1125" fill="var(--backdrop)"/>

  <g class="halo">
    <rect x="341" y="61" width="523" height="1042"/>
    <polygon points="341,78 200,88 201,242 316,272 327,282 346,282"/>
    <polygon points="864,66 878,66 888,79 1003,108 1003,265 868,273"/>
    <path d="M871,279 H1076 V284 Q1125,288 1150,325 V530 Q1125,568 1078,572 V575 H871 Z"/>
    <polygon points="347,583 328,583 319,594 203,625 203,781 341,789 347,795"/>
    <polygon points="863,578 871,588 1004,594 1006,750 890,781 878,793 863,794"/>
    <path d="M347,799 H128 V802 Q80,806 58,842 V1060 Q80,1094 128,1097 V1100 H347 Z"/>
    <polygon points="353,1103 363,1147 847,1146 859,1103"/>
  </g>

  <polygon class="cut" points="341,78 200,88 201,242 316,272 327,282 346,282"/>
  <polygon class="cut" points="864,66 878,66 888,79 1003,108 1003,265 868,273"/>
  <path class="cut" d="M1076,284 Q1125,288 1150,325 V530 Q1125,568 1078,572"/>
  <polygon class="cut" points="347,583 328,583 319,594 203,625 203,781 341,789 347,795"/>
  <polygon class="cut" points="863,578 871,588 1004,594 1006,750 890,781 878,793 863,794"/>
  <path class="cut" d="M128,802 Q80,806 58,842 V1060 Q80,1094 128,1097"/>
  <polygon class="cut" points="353,1103 363,1147 847,1146 859,1103"/>

  <use href="#lid-artwork" x="341" y="61"/>
  <use href="#lid-artwork" x="347" y="578"/>

  <use href="#front-artwork" x="346" y="280"/>
  <text class="tagline" x="603" y="409" text-anchor="middle">Merry</text>
  <text class="headline" x="603" y="435" text-anchor="middle">Christmas</text>

  <use href="#front-artwork" transform="translate(347 1098) scale(1 -1)"/>
  <g transform="rotate(180 604 956)">
    <text class="tagline" x="604" y="947" text-anchor="middle">Merry</text>
    <text class="headline" x="604" y="973" text-anchor="middle">Christmas</text>
  </g>

  <rect x="871" y="279" width="205" height="296" fill="var(--panel-light)"/>
  <text class="logo-placeholder" transform="translate(986 427) rotate(-90)" text-anchor="middle">LOGO</text>
  <rect x="128" y="799" width="219" height="301" fill="var(--panel-light)"/>
  <text class="logo-placeholder" transform="translate(222 950) rotate(90)" text-anchor="middle">LOGO</text>

  <g stroke="var(--die-line)" stroke-width="1" fill="none">
    <line x1="346" y1="282" x2="346" y2="575"/>
    <line x1="346" y1="798" x2="346" y2="1100"/>
    <line x1="784" y1="576" x2="1076" y2="575"/>
    <line x1="128" y1="798" x2="555" y2="798"/>
    <line x1="792" y1="798" x2="863" y2="798"/>
  </g>
</svg>
</body>
</html>
```